Website Design for a New Business Sharing Application

Purpose: Website for a new product – a sharing application called "Pondly.io"

Product concept: Easy sharing of business information. The application has different sections: tasks, calendars, documents, contacts, notes and links. The key feature of the application is that you can drag and drop information from different sections into a "share." A share is a page which lists all the types of information that you drag into it. You can add people to this "share."

Note: The application itself is not part of this project, just the website.

Website details: The site, in addition to being informational, will actually be the first point of entry for visitors into the application itself. Because of that, we would like the website design to reflect the look of the application, to create a smooth and seamless experience for the user moving from the website into the application (tough the website does not need to look *exactly* like the application). Included Product Tour screenshots show you the look of the application.

Website pages to be created: 4 pages
We are flexible in terms of the exact structure and placement of elements. You may change that any way you like. The pages are as follows:

Home page
Product Tour page
Press page
Blog page

Specific description of pages are provided in project files we will upload. We will also upload the logo, home page layout we have in mind, and other supporting files.

NOTE: Please submit first the design of the home page. Based on this design we will ask selected designers to submit designs for the other pages.

Target Market(s)

Business people who want to share work related files with their colleagues

Industry/Entity Type

Business

Requirements
Must have
• All the required features are listed in the description of the website and specific pages that we will upload.

```html
<!DOCTYPE html>
<html lang="en">
<head>
<meta charset="utf-8">
<title>Pondly.io – Share NOW!</title>
<link rel="stylesheet" href="https://fonts.googleapis.com/css2?family=Source+Sans+3:wght@400;600;700&family=Nanum+Pen+Script&display=swap">
<style>
  :root {
    --band: #efefef;
    --page: #ffffff;
    --ink: #444444;
    --ink-soft: #6f6f6f;
    --ink-mute: #9a9a9a;
    --dash: #bdbdbd;
    --brand: #1f7fc4;
    --brand-dot: #e8731f;
    --drop-blue: #7cb9e2;
    --drop-panel: #f1f1f1;
    --panel-edge: #cfcfcf;
    --mail-purple: #9a80c8;
    --go-green: #8fd170;
    --go-green-dark: #79bf5a;
    --note-blue: #1e4fa8;
    --note-red: #d2262b;
    --c-files: #4fa6d9;
    --c-pictures: #7a4fa8;
    --c-tasks: #b4282c;
    --c-todos: #d0a03a;
    --c-calendars: #a54fbf;
    --c-notes: #3a74b8;
    --c-links: #6fb63c;
    --arrow: #9a9a9a;
    --social: #b8b8b8;
  }
  * { box-sizing: border-box; margin: 0; padding: 0; }
  html, body { width: 1200px; height: 675px; overflow: hidden; background: var(--page); }
  body { position: relative; font-family: "Source Sans 3", "Myriad Pro", sans-serif; color: var(--ink); }

  .site-header { position: absolute; left: 0; top: 0; width: 1200px; height: 85px; background: var(--band); }
  .brand { position: absolute; left: 80px; top: 22px; display: flex; align-items: center; gap: 10px; }
  .brand-dot { width: 30px; height: 30px; border-radius: 50%; background: var(--brand-dot); }
  .brand-name { font-size: 30px; font-weight: 700; color: var(--brand); letter-spacing: -0.3px; }
  .header-link { position: absolute; right: 55px; top: 24px; font-size: 31px; color: var(--ink-soft); font-weight: 400; }

  .hero-badge { position: absolute; left: 147px; top: 192px; width: 485px; height: 116px;
    border: 3px dashed var(--dash); border-radius: 16px;
    display: flex; align-items: center; justify-content: center;
    font-size: 82px; font-weight: 700; color: var(--ink-soft); letter-spacing: -1px; }
  .hero-tagline { position: absolute; left: 88px; top: 352px; font-size: 35px; font-weight: 700; color: #787878; letter-spacing: -0.3px; }

  .content-types { position: absolute; left: 128px; top: 418px; display: flex; align-items: center; gap: 7px; font-size: 21px; }
  .content-types .sep { color: var(--arrow); font-size: 13px; }
  .t-files { color: var(--c-files); } .t-pictures { color: var(--c-pictures); } .t-tasks { color: var(--c-tasks); }
  .t-todos { color: var(--c-todos); } .t-calendars { color: var(--c-calendars); } .t-notes { color: var(--c-notes); } .t-links { color: var(--c-links); }

  .video-cta { position: absolute; left: 300px; top: 499px; display: flex; align-items: center; gap: 6px; font-size: 15px; color: var(--ink-soft); }
  .video-button { display: flex; align-items: center; height: 22px; border: 1px solid #bbb; border-radius: 3px; background: linear-gradient(#fafafa, #e6e6e6); font-size: 14px; color: #333; overflow: hidden; }
  .video-button span { padding: 0 6px; }
  .video-button i { display: flex; align-items: center; justify-content: center; width: 18px; height: 100%; background: var(--drop-blue); }

  .hand-note { position: absolute; font-family: "Nanum Pen Script", cursive; color: var(--note-blue); font-size: 22px; line-height: 18px; transform: rotate(-12deg); transform-origin: left top; }
  .note-fast { left: 527px; top: 494px; }
  .note-social { left: 540px; top: 548px; }

  .share-panel { position: absolute; left: 769px; width: 306px; height: 104px; border: 1px solid var(--panel-edge); background: linear-gradient(90deg, #f8f8f8, #ececec); }
  .drop-zone { top: 186px; }
  .email-signup { top: 396px; }
  .panel-icon { position: absolute; left: 0; top: 0; width: 63px; height: 102px; display: flex; align-items: center; justify-content: center; }
  .drop-zone .panel-icon { background: var(--drop-blue); }
  .email-signup .panel-icon { background: var(--mail-purple); }
  .drop-text { position: absolute; left: 99px; top: 27px; font-size: 20px; line-height: 25px; color: #555; }
  .or-divider { position: absolute; left: 898px; top: 310px; font-size: 50px; color: var(--ink-mute); }
  .email-label { position: absolute; left: 77px; top: 8px; font-size: 12px; color: #333; }
  .email-field { position: absolute; left: 77px; top: 28px; width: 211px; height: 20px; border: 1px solid #c6c6c6; background: #fff; font-size: 12px; color: #8a8a8a; padding: 2px 6px; }
  .start-button { position: absolute; left: 77px; top: 56px; width: 211px; height: 39px; background: var(--go-green); border: 1px solid var(--go-green-dark); color: #fff; font-size: 26px; display: flex; align-items: center; justify-content: center; }

  .site-footer { position: absolute; left: 0; top: 600px; width: 1200px; height: 75px; background: var(--band); }
  .footer-nav { position: absolute; left: 115px; top: 28px; display: flex; gap: 7px; font-size: 14.5px; color: var(--ink); }
  .footer-nav .bar { color: #777; }
  .footer-nav .struck { position: relative; }
  .footer-nav .struck::after { content: ""; position: absolute; left: -2px; right: -2px; top: 9px; height: 2px; background: var(--note-red); transform: rotate(-3deg); }
  .note-free { position: absolute; left: 320px; top: 598px; font-family: "Nanum Pen Script", cursive; color: var(--note-red); font-size: 17px; line-height: 13px; transform: rotate(-10deg); transform-origin: left top; }
  .social-links { position: absolute; left: 1008px; top: 620px; display: flex; gap: 13px; }
  .social-links span { width: 31px; height: 31px; border-radius: 4px; background: var(--social); }
</style>
</head>
<body>
  <header class="site-header">
    <div class="brand"><span class="brand-dot"></span><span class="brand-name">Pondly.io</span></div>
    <div class="header-link">Access your shares</div>
  </header>

  <main>
    <div class="hero-badge">Share NOW!</div>
    <p class="hero-tagline">Drag information, add people, BOOM!</p>
    <div class="content-types">
      <span class="t-files">files</span><span class="sep">▶</span>
      <span class="t-pictures">pictures</span><span class="sep">▶</span>
      <span class="t-tasks">tasks</span><span class="sep">▶</span>
      <span class="t-todos">to-dos</span><span class="sep">▶</span>
      <span class="t-calendars">calendars</span><span class="sep">▶</span>
      <span class="t-notes">notes</span><span class="sep">▶</span>
      <span class="t-links">links</span>
    </div>
    <div class="video-cta">What is it?
      <span class="video-button"><span>Watch Video</span><i><svg width="8" height="10" viewBox="0 0 8 10"><path d="M0 0 L8 5 L0 10Z" fill="#fff"/></svg></i></span>
    </div>
    <p class="hand-note note-fast">&gt;&gt; Certified fastest<br>&nbsp;&nbsp;&nbsp;&nbsp;sharing in the market</p>
    <p class="hand-note note-social">&gt;&gt; Its social!</p>

    <section class="share-panel drop-zone">
      <div class="panel-icon">
        <svg width="44" height="48" viewBox="0 0 44 48">
          <path d="M14 6 H24 L28 10 H40 V36 H14 Z" fill="none" stroke="#fff" stroke-width="1.6"/>
          <rect x="4" y="27" width="22" height="6" fill="#f4d23c"/>
          <rect x="12" y="19" width="6" height="22" fill="#f4d23c"/>
        </svg>
      </div>
      <p class="drop-text">Drag files here to<br>share immediately</p>
    </section>

    <div class="or-divider">or</div>

    <section class="share-panel email-signup">
      <div class="panel-icon">
        <svg width="50" height="48" viewBox="0 0 50 48">
          <rect x="14" y="6" width="30" height="22" fill="#fff"/>
          <path d="M14 6 L29 19 L44 6" fill="none" stroke="#9a80c8" stroke-width="1.5"/>
          <path d="M4 30 L12 24 V28 H22 V32 H12 V36Z" fill="#8fd170"/>
          <path d="M40 38 L32 32 V36 H22 V40 H32 V44Z" fill="#8fd170"/>
        </svg>
      </div>
      <label class="email-label">Enter business email</label>
      <div class="email-field">jmarlow@mailbox.net</div>
      <div class="start-button">Start Sharing</div>
    </section>
  </main>

  <footer class="site-footer">
    <nav class="footer-nav">
      <span>Home</span><span class="bar">|</span><span>About Us</span><span class="bar">|</span>
      <span>Product Tour</span><span class="bar">|</span><span class="struck">Pricing</span><span class="bar">|</span>
      <span>Terms Of Use</span><span class="bar">|</span><span>Jobs</span><span class="bar">|</span>
      <span>Sign Up</span><span class="bar">|</span><span>Blog</span><span class="bar">|</span>
      <span>Press</span><span class="bar">|</span><span>Contact Us</span>
    </nav>
    <div class="social-links" aria-label="Social links"><span></span><span></span><span></span></div>
  </footer>
  <p class="note-free">Free for<br>unlimited users</p>
</body>
</html>
```